Security business needs NDA formatted.

We need our NDA formatted properly and to look modern with our logo. Anybody can paste words into a document, but we need something clean, modern, DocuSign-friendly, and stylish.

```html
<!DOCTYPE html>
<html lang="en">
<head>
<meta charset="utf-8">
<title>Terravane — Non-Disclosure Agreement</title>
<link rel="stylesheet" href="https://fonts.googleapis.com/css2?family=Montserrat:wght@400;600;700&display=swap">
<style>
:root{
  --ink:#1f1d1e;
  --paper:#ffffff;
  --stage:#a4a4a4;
  --band:#dcdcdc;
  --bar:#8c8c8c;
  --rule:#c8c8c8;
  --muted:#5a5a5a;
  --faint:#ececec;
}
*{box-sizing:border-box;margin:0;padding:0}
html,body{width:1200px;height:2983px;overflow:hidden}
body{background:var(--stage);font-family:"Montserrat",sans-serif;color:var(--ink)}
.canvas{position:relative;width:1200px;height:2983px;overflow:hidden;background:var(--stage)}
.stage-top{position:absolute;left:0;top:0;width:1200px;height:740px;background:linear-gradient(180deg,#c9c9c9,#b4b4b4)}

/* brand */
.brand{display:flex;align-items:center;gap:6px}
.brand-dot{border-radius:50%;background:var(--ink);flex:none}
.brand-name{font-weight:700;line-height:1}
.brand-tag{font-weight:600;letter-spacing:.06em;margin-top:2px}
.brand-text{border-left:1px solid currentColor;padding-left:5px}

/* front cover (flat) */
.cover-flat{position:absolute;left:330px;top:60px;width:415px;height:610px;background:var(--ink);color:#fff}
.cover-flat .tab{position:absolute;left:73px;top:0;width:197px;height:221px;background:var(--paper);display:flex;align-items:flex-end;justify-content:center;padding-bottom:42px;color:var(--ink)}
.cover-flat .tab .brand-dot{width:34px;height:34px}
.cover-flat .tab .brand-name{font-size:19px}
.cover-flat .tab .brand-tag{font-size:5.5px}
.cover-flat .title{position:absolute;left:73px;top:235px;font-size:21px;font-weight:700;line-height:1.2;letter-spacing:.01em}
.cover-flat .pattern{position:absolute;left:20px;right:20px;top:325px;bottom:20px;background:linear-gradient(160deg,#2a2829,#1f1d1e 70%)}
.cover-flat .pin{position:absolute;left:110px;top:540px}

/* pages */
.page{position:absolute;width:373px;height:527px;background:var(--paper);overflow:hidden}
.page::before{content:"";position:absolute;left:0;top:0;right:0;height:14px;background:var(--band)}
.page-head{position:absolute;left:16px;top:30px;color:var(--ink)}
.page-head .brand-dot{width:25px;height:25px}
.page-head .brand-name{font-size:14px}
.page-head .brand-tag{font-size:4px}
.page-pin{position:absolute;left:26px;top:170px;opacity:.35}
.page-foot{position:absolute;left:0;right:0;bottom:0;height:26px;background:var(--bar)}
.page-foot span{display:block;width:104px;height:26px;background:#4d4d4d;color:#fff;font-size:5px;line-height:26px;padding-left:18px}
.page-body{position:absolute;left:75px;right:18px;top:80px;font-size:5.6px;line-height:1.38}
.page-body p{margin-bottom:4px}
.clause{display:flex;gap:6px;margin-bottom:4px}
.clause>b{font-weight:400;min-width:8px}
.sub{padding-left:12px}
.sub2{padding-left:26px}
.section{display:flex;align-items:center;gap:6px;background:var(--band);font-weight:700;font-size:7px;height:15px;padding-left:4px;margin:10px 0 7px -8px;text-transform:uppercase}
.section::before{content:"";width:8px;height:8px;border-radius:50%;background:var(--ink)}
.strong{font-weight:700}

/* page 1 specifics */
.parties{background:#efefef;padding:10px 9px 12px;margin-top:12px;font-size:5.2px}
.parties h3{font-size:7px;margin-bottom:8px}
.parties .line{border-bottom:1px solid var(--muted);height:14px;margin:0 30px 3px 0}
.dated{display:flex;gap:6px;align-items:flex-end;margin-top:8px}
.dated i{display:inline-block;border-bottom:1px solid var(--muted);width:58px}
.background{background:var(--ink);color:#fff;margin-top:24px;padding:8px 9px 12px;font-size:5.4px}
.background h3{background:var(--band);color:var(--ink);font-size:7px;height:14px;line-height:14px;padding-left:6px;margin-bottom:7px}

/* notices / signature */
.field{display:flex;gap:4px;align-items:flex-end;margin:4px 0 0 24px}
.field em{font-style:normal;width:30px;text-align:right}
.field i{flex:1;border-bottom:1px solid var(--muted);height:8px;font-style:normal}
.sign{margin-top:8px}
.sign .row{display:flex;align-items:flex-end;gap:6px;margin-top:6px}
.sign .row span{width:28px}
.sign .row i{flex:1;border-bottom:1px solid var(--muted);height:8px;font-style:normal}

/* grid cover page */
.page-cover::before{display:none}
.page-cover .block{position:absolute;left:67px;top:0;width:173px;height:198px;background:var(--ink);color:#fff;display:flex;align-items:flex-end;justify-content:center;padding-bottom:12px}
.page-cover .block .brand-dot{width:26px;height:26px;background:#fff}
.page-cover .block .brand-name{font-size:14px}
.page-cover .block .brand-tag{font-size:4px}
.page-cover .title{position:absolute;left:67px;top:212px;font-size:17px;font-weight:700;line-height:1.25}
.page-cover .pattern{position:absolute;left:0;right:0;top:270px;bottom:0;background:linear-gradient(180deg,#fafafa,#f1f1f1)}
.page-cover .pin{position:absolute;left:100px;top:470px}

/* back cover */
.back{position:absolute;left:25px;top:2380px;width:399px;height:561px;background:var(--ink);color:#fff;display:flex;flex-direction:column;align-items:center;justify-content:center;gap:12px}
.back .disc{width:120px;height:120px;border-radius:50%;background:#fff}
.back .name{font-size:16px;font-weight:700}
.back .web{font-size:8px;font-weight:600}
</style>
</head>
<body>
<main class="canvas">
  <div class="stage-top"></div>

  <!-- Front cover, flat -->
  <section class="cover-flat">
    <div class="tab">
      <div class="brand">
        <span class="brand-dot"></span>
        <div class="brand-text"><div class="brand-name">Terravane</div><div class="brand-tag">Spatial Security Intelligence</div></div>
      </div>
    </div>
    <h1 class="title">NON-DISCLOSURE<br>AGREEMENT</h1>
    <div class="pattern" role="img" aria-label="Fine diagonal line grid pattern"></div>
    <svg class="pin" width="34" height="42" viewBox="0 0 34 42" aria-hidden="true"><path d="M17 1C8 1 2 8 2 16c0 11 15 25 15 25s15-14 15-25C32 8 26 1 17 1z" fill="#fff"/><circle cx="17" cy="16" r="6" fill="#1f1d1e"/></svg>
  </section>

  <!-- Page: cover -->
  <article class="page page-cover" style="left:25px;top:758px">
    <div class="block">
      <div class="brand">
        <span class="brand-dot"></span>
        <div class="brand-text"><div class="brand-name">Terravane</div><div class="brand-tag">Spatial Security Intelligence</div></div>
      </div>
    </div>
    <h2 class="title">NON-DISCLOSURE<br>AGREEMENT</h2>
    <div class="pattern" role="img" aria-label="Light diagonal line grid pattern"></div>
    <svg class="pin" width="30" height="38" viewBox="0 0 34 42" aria-hidden="true"><path d="M17 1C8 1 2 8 2 16c0 11 15 25 15 25s15-14 15-25C32 8 26 1 17 1z" fill="#c9c9c9"/><circle cx="17" cy="16" r="6" fill="#fff"/></svg>
  </article>

  <!-- Page 1 -->
  <article class="page" style="left:413px;top:758px">
    <header class="page-head"><div class="brand"><span class="brand-dot"></span><div class="brand-text"><div class="brand-name">Terravane</div><div class="brand-tag">Spatial Security Intelligence</div></div></div></header>
    <svg class="page-pin" width="26" height="32" viewBox="0 0 34 42" aria-hidden="true"><path d="M17 1C8 1 2 8 2 16c0 11 15 25 15 25s15-14 15-25C32 8 26 1 17 1z" fill="#cfcfcf"/><circle cx="17" cy="16" r="6" fill="#fff"/></svg>
    <div class="page-body" style="top:120px">
      <p><span class="strong">THIS NON-DISCLOSURE AGREEMENT</span> ("the Agreement")</p>
      <div class="dated">Dated this <i></i> day of <i></i> <i></i></div>
      <div class="parties">
        <h3>BETWEEN:</h3>
        <p>Northline Labs of 58 Harbor Road, CA, 90210, USA (the <b>"Company"</b>)<br>OF THE FIRST PART</p>
        <p class="strong" style="margin:10px 0 14px">- AND -</p>
        <div class="line"></div>
        <p>(the <b>"Evaluator"</b>)<br>OF THE SECOND PART</p>
      </div>
      <div class="background">
        <h3>BACKGROUND</h3>
        <p>A.&nbsp; Northline Labs has proprietary information and know-how relating to certain investigation tools and tactics (the "Company").</p>
        <p>B.&nbsp; In connection with the Evaluator evaluating the Invention for possible patent, development, and marketing (the "Permitted Purpose"), the Evaluator has requested certain confidential information (the "Confidential Information") regarding the Company.</p>
      </div>
    </div>
    <footer class="page-foot"><span>©2024 Terravane Legal // 1</span></footer>
  </article>

  <!-- Page 2 -->
  <article class="page" style="left:801px;top:758px">
    <header class="page-head"><div class="brand"><span class="brand-dot"></span><div class="brand-text"><div class="brand-name">Terravane</div><div class="brand-tag">Spatial Security Intelligence</div></div></div></header>
    <svg class="page-pin" width="26" height="32" viewBox="0 0 34 42" aria-hidden="true"><path d="M17 1C8 1 2 8 2 16c0 11 15 25 15 25s15-14 15-25C32 8 26 1 17 1z" fill="#cfcfcf"/><circle cx="17" cy="16" r="6" fill="#fff"/></svg>
    <div class="page-body">
      <p><b>IN CONSIDERATION OF</b> and as a condition of the Company providing the Confidential Information to the Evaluator in addition to other valuable consideration, the receipt and sufficiency of which consideration is hereby acknowledged, the parties to this Agreement agree as follows:</p>
      <div class="section">Confidential Information</div>
      <div class="clause"><b>1.</b><span>All written and oral information and materials disclosed or provided by the Company to the Evaluator under this Agreement constitute Confidential Information regardless of whether such information was provided before or after the date of this Agreement or how it was provided to the Evaluator.</span></div>
      <div class="clause"><b>2.</b><span>'Confidential Information' means all data and information relating to the invention as well as data and information relating to the Company, including but not limited to, the following:</span></div>
      <div class="clause sub"><b>a)</b><span><b>'Business Operations'</b> which includes internal personnel and financial information of the Company, vendor names and other vendor information, purchasing and internal cost information, internal services and operational manuals, external business contacts including those stored on social media accounts or other similar platforms, and the manner and methods of conducting the Company's business;</span></div>
      <div class="clause sub"><b>b)</b><span><b>'Customer Information'</b> which includes names of customers of the Company, their representatives, all customer contact information, contracts and their contents and parties, customer services, data provided by customers and the type, quantity and specifications of products and services purchased, leased or received by customers of the Company;</span></div>
      <div class="clause sub"><b>c)</b><span><b>'Intellectual Property'</b> which includes information relating to the Company's proprietary rights prior to any public disclosure of such information, including the nature of the proprietary rights, production data, technical and engineering data, test data and test results, the status and details of research and development of products and services, and information regarding acquiring, protecting, enforcing and licensing proprietary rights;</span></div>
      <div class="clause sub"><b>d)</b><span><b>'Service Information'</b> which includes all data and information relating to the services provided by the Company, including plans, schedules, manpower, inspection, and training information;</span></div>
      <div class="clause sub"><b>e)</b><span><b>'Product Information'</b> which includes all specifications for products of the Company as well as work product resulting from or related to work or projects of the Company, of any type or form in any stage of actual or anticipated research and development;</span></div>
    </div>
    <footer class="page-foot"><span>©2024 Terravane Legal // 2</span></footer>
  </article>

  <!-- Page 3 -->
  <article class="page" style="left:25px;top:1299px">
    <header class="page-head"><div class="brand"><span class="brand-dot"></span><div class="brand-text"><div class="brand-name">Terravane</div><div class="brand-tag">Spatial Security Intelligence</div></div></div></header>
    <svg class="page-pin" width="26" height="32" viewBox="0 0 34 42" aria-hidden="true"><path d="M17 1C8 1 2 8 2 16c0 11 15 25 15 25s15-14 15-25C32 8 26 1 17 1z" fill="#cfcfcf"/><circle cx="17" cy="16" r="6" fill="#fff"/></svg>
    <div class="page-body">
      <div class="clause sub"><b>f)</b><span><b>'Production Processes'</b> which includes processes used in the creation, production and manufacturing of the work product of the Company, including formulas, patterns, molds, models, methods, techniques, specifications, processes, procedures, equipment, devices, programs, and designs;</span></div>
      <div class="clause sub"><b>g)</b><span><b>'Accounting Information'</b> which includes all financial statements, annual reports, balance sheets, company asset information, company liability information, revenue and expense reporting, profit and loss reporting, cash flow reporting, accounts receivable, accounts payable, purchasing information and payroll information of the Company;</span></div>
      <div class="clause sub"><b>h)</b><span><b>'Marketing and Development Information'</b> which includes marketing and development plans of the Company, price and cost data, price and fee amounts, pricing and billing policies, quoting procedures, marketing techniques and methods of obtaining business, forecasts and forecast assumptions and volumes, and future plans and potential strategies of the Company which have been or are being discussed;</span></div>
      <div class="clause sub"><b>i)</b><span><b>'Computer Technology'</b> which includes all scientific and technical information or material of the Company pertaining to any machine, appliance or process, including specifications, proposals, models, designs, formulas, test results and reports, analyses, simulation results, tables of operating conditions, materials, components, industrial skills, operating and testing procedures, shop practices, know-how and show-how;</span></div>
      <div class="clause sub"><b>j)</b><span><b>'Proprietary Computer Code'</b> which includes all sets of statements, instructions or programs of the Company, whether in human readable or machine readable form, that are expressed, fixed, embodied or stored in any manner and that can be used directly or indirectly in a computer ('Computer Programs'); any report format, design or drawing created or produced by such Computer Programs; and all documentation, design specifications and charts, and operating procedures which support the Computer Programs; and</span></div>
      <div class="clause sub"><b>k)</b><span>Confidential Information will also include any information that has been disclosed by a third party to the Company and is protected by a non-disclosure agreement entered into between the third party and the Company.</span></div>
    </div>
    <footer class="page-foot"><span>©2024 Terravane Legal // 3</span></footer>
  </article>

  <!-- Page 4 -->
  <article class="page" style="left:413px;top:1299px">
    <header class="page-head"><div class="brand"><span class="brand-dot"></span><div class="brand-text"><div class="brand-name">Terravane</div><div class="brand-tag">Spatial Security Intelligence</div></div></div></header>
    <svg class="page-pin" width="26" height="32" viewBox="0 0 34 42" aria-hidden="true"><path d="M17 1C8 1 2 8 2 16c0 11 15 25 15 25s15-14 15-25C32 8 26 1 17 1z" fill="#cfcfcf"/><circle cx="17" cy="16" r="6" fill="#fff"/></svg>
    <div class="page-body">
      <div class="clause"><b>3.</b><span>Confidential Information will not include the following information:</span></div>
      <div class="clause sub"><b>a)</b><span>Information that is generally known in the industry of the Company;</span></div>
      <div class="clause sub"><b>b)</b><span>Information that is now or subsequently becomes generally available to the public through no wrongful act of the Evaluator;</span></div>
      <div class="clause sub"><b>c)</b><span>Information rightly in the possession of the Evaluator prior to the disclosure to the Evaluator by the Company;</span></div>
      <div class="clause sub"><b>d)</b><span>Information that is independently created by the Evaluator without direct or indirect use of the Confidential Information; or</span></div>
      <div class="clause sub"><b>e)</b><span>Information that the Evaluator rightfully obtains from a third party who has the right to transfer or disclose it.</span></div>
      <div class="section">Obligations of Non-Disclosure</div>
      <div class="clause"><b>4.</b><span>Except as otherwise provided in this Agreement, the Evaluator must not disclose the Confidential Information.</span></div>
      <div class="clause"><b>5.</b><span>Except as otherwise provided in this Agreement, the Confidential Information will remain the exclusive property of the Company and will only be used by the Evaluator for the Permitted Purpose. The Evaluator will not use the Confidential Information for any purpose that might be directly or indirectly detrimental to the Company or any associated affiliates or subsidiaries.</span></div>
      <div class="clause"><b>6.</b><span>The obligations to ensure and prevent the disclosure of the Confidential Information imposed on the Evaluator in this Agreement and any obligations to provide notice under this Agreement will survive the expiration or termination, as the case may be, of this Agreement and those obligations will last indefinitely.</span></div>
      <div class="clause"><b>7.</b><span>The Evaluator may disclose any of the Confidential Information:</span></div>
      <div class="clause sub"><b>a)</b><span>to such employees, agents, representatives and advisors of the Evaluator that have a need to know for the Permitted Purpose provided that:</span></div>
      <div class="clause sub2"><b>i.</b><span>the Evaluator has informed such personnel of the confidential nature of the Confidential Information;</span></div>
      <div class="clause sub2"><b>ii.</b><span>such personnel agree to be legally bound to the same burdens of non-disclosure and non-use as the Evaluator;</span></div>
      <div class="clause sub2"><b>iii.</b><span>the Evaluator agrees to take all necessary steps to ensure that the terms of this Agreement are not violated by such personnel; and</span></div>
      <div class="clause sub2"><b>iv.</b><span>the Evaluator agrees to be responsible for and indemnify the Company for any breach of this Agreement by its personnel.</span></div>
      <div class="clause sub"><b>b)</b><span>to a third party where the Company has consented in writing to such disclosure; and</span></div>
    </div>
    <footer class="page-foot"><span>©2024 Terravane Legal // 4</span></footer>
  </article>

  <!-- Page 5 -->
  <article class="page" style="left:801px;top:1299px">
    <header class="page-head"><div class="brand"><span class="brand-dot"></span><div class="brand-text"><div class="brand-name">Terravane</div><div class="brand-tag">Spatial Security Intelligence</div></div></div></header>
    <svg class="page-pin" width="26" height="32" viewBox="0 0 34 42" aria-hidden="true"><path d="M17 1C8 1 2 8 2 16c0 11 15 25 15 25s15-14 15-25C32 8 26 1 17 1z" fill="#cfcfcf"/><circle cx="17" cy="16" r="6" fill="#fff"/></svg>
    <div class="page-body">
      <div class="clause sub"><b>c)</b><span>to the extent required by law or by the request or requirement of any judicial, legislative, administrative or other governmental body.</span></div>
      <div class="clause"><b>8.</b><span>The Evaluator agrees to retain all Confidential Information at its usual place of business and to store all Confidential Information separate from other information and documents held in the same location. Further, the Confidential Information may not be used, reproduced, transformed, or stored on a computer or device that is accessible to persons to whom disclosure may not be made, as set out in this Agreement.</span></div>
      <div class="section">Non-Solicitation</div>
      <div class="clause"><b>9.</b><span>The Evaluator, its affiliates, subsidiaries and representatives will not, from the date of this Agreement for a period of two years, directly or indirectly solicit for employment or employ any person who is now employed or retained by the Company or any affiliate of the Company without the prior written consent of the Company.</span></div>
      <div class="section">Non-Competition</div>
      <div class="clause"><b>10.</b><span>Other than with the express written consent of the Company, which consent may not be unreasonably withheld, the Evaluator will not, from the date of this Agreement for a period of two years, be directly or indirectly involved with a business which is in direct competition with the Company in the market for the Invention.</span></div>
      <div class="section">Ownership and Title</div>
      <div class="clause"><b>11.</b><span>Nothing contained in this Agreement will grant to or create in the Evaluator, either expressly or impliedly, any right, title, interest or license in or to the intellectual property of the Company.</span></div>
      <div class="section">Remedies</div>
      <div class="clause"><b>12.</b><span>The Evaluator agrees and acknowledges that the Confidential Information is of a proprietary and confidential nature and that any disclosure of the Confidential Information to a third party in breach of this Agreement cannot be reasonably or adequately compensated for in money damages and would cause irreparable injury to the Company. Accordingly, the Evaluator agrees that the Company is entitled to, in addition to all other rights and remedies available to it at law or in equity, an injunction restraining the Evaluator, any of its personnel, and any agents of the Evaluator, from directly or indirectly committing or engaging in any act restricted by this Agreement in relation to the Confidential Information.</span></div>
    </div>
    <footer class="page-foot"><span>©2024 Terravane Legal // 5</span></footer>
  </article>

  <!-- Page 6 -->
  <article class="page" style="left:25px;top:1839px">
    <header class="page-head"><div class="brand"><span class="brand-dot"></span><div class="brand-text"><div class="brand-name">Terravane</div><div class="brand-tag">Spatial Security Intelligence</div></div></div></header>
    <svg class="page-pin" width="26" height="32" viewBox="0 0 34 42" aria-hidden="true"><path d="M17 1C8 1 2 8 2 16c0 11 15 25 15 25s15-14 15-25C32 8 26 1 17 1z" fill="#cfcfcf"/><circle cx="17" cy="16" r="6" fill="#fff"/></svg>
    <div class="page-body" style="top:70px">
      <div class="section" style="margin-top:0">Return of Confidential Information</div>
      <div class="clause"><b>13.</b><span>The Company may at any time request the return of all Confidential Information from the Evaluator. Upon the request of the Company, or in the event that the Evaluator ceases to require use of the Confidential Information, or upon the expiration or termination of this Agreement, the Evaluator will:</span></div>
      <div class="clause sub"><b>a)</b><span>return all Confidential Information to the Company;</span></div>
      <div class="clause sub"><b>b)</b><span>provide a certificate to the Company to the effect that the Evaluator has returned all Confidential Information to the Company.</span></div>
      <div class="section">Notices</div>
      <div class="clause"><b>14.</b><span>In the event that the Evaluator is required in a civil, criminal or regulatory proceeding to disclose any part of the Confidential Information, the Evaluator will give to the Company prompt written notice of such request so the Company may seek an appropriate remedy or alternatively to waive the Evaluator's compliance with the provisions of this Agreement in regards to the request.</span></div>
      <div class="clause"><b>15.</b><span>If the Evaluator loses or makes unauthorized disclosure of any of the Confidential Information, the Evaluator will immediately notify the Company and take all reasonable steps necessary to retrieve the lost or improperly disclosed Confidential Information.</span></div>
      <div class="clause"><b>16.</b><span>Any notices or delivery required in this Agreement will be deemed completed when hand-delivered, delivered by agent, or seven days after being placed in the post, postage prepaid, to the parties at the addresses contained in this Agreement or as the parties may later designate in writing.</span></div>
      <div class="clause"><b>17.</b><span>The addresses for any notice to be delivered to any of the parties to this Agreement are as follows:</span></div>
      <div class="field"><em><b>a) Name:</b></em><i>Northline Labs</i></div>
      <div class="field"><em>Address:</em><i>1190 Larch Ave, Fenwick, MI 48000, USA</i></div>
      <div class="field"><em><b>b) Name:</b></em><i></i></div>
      <div class="field" style="margin-bottom:4px"><em>Address:</em><i></i></div>
      <div class="section">Representations</div>
      <div class="clause"><b>18.</b><span>In providing the Confidential Information, the Company makes no representations, either expressly or impliedly as to its adequacy, sufficiency, completeness, correctness or its lack of defect of any kind, including any patent or trademark infringement that may result from the use of such information.</span></div>
    </div>
    <footer class="page-foot"><span>©2024 Terravane Legal // 6</span></footer>
  </article>

  <!-- Page 7 -->
  <article class="page" style="left:413px;top:1839px">
    <header class="page-head"><div class="brand"><span class="brand-dot"></span><div class="brand-text"><div class="brand-name">Terravane</div><div class="brand-tag">Spatial Security Intelligence</div></div></div></header>
    <svg class="page-pin" width="26" height="32" viewBox="0 0 34 42" aria-hidden="true"><path d="M17 1C8 1 2 8 2 16c0 11 15 25 15 25s15-14 15-25C32 8 26 1 17 1z" fill="#cfcfcf"/><circle cx="17" cy="16" r="6" fill="#fff"/></svg>
    <div class="page-body" style="top:70px">
      <div class="section" style="margin-top:0">Further Agreements</div>
      <div class="clause"><b>19.</b><span>In the event that the Evaluator finds that the Invention is worthy of being patented, developed and marketed, the Company and the Evaluator may negotiate an additional agreement to define all their respective rights regarding such patenting, marketing, and development.</span></div>
      <div class="section">Termination</div>
      <div class="clause"><b>20.</b><span>Either party may terminate this Agreement by providing written notice to the other party. Except as otherwise provided in this Agreement, all rights and obligations under this Agreement will terminate at that time.</span></div>
      <div class="section">Assignment</div>
      <div class="clause"><b>21.</b><span>Except where a party has changed its corporate name or merged with another corporation, this Agreement may not be assigned or otherwise transferred by either party in whole or part without the prior written consent of the other party to this Agreement.</span></div>
      <div class="section">Amendments</div>
      <div class="clause"><b>22.</b><span>This Agreement may only be amended or modified by a written instrument executed by both the Company and the Evaluator.</span></div>
      <div class="section">Governing Law</div>
      <div class="clause"><b>23.</b><span>This Agreement will be construed in accordance with and governed by the laws of the State of Michigan.</span></div>
      <div class="section">General Provisions</div>
      <div class="clause"><b>24.</b><span>Time is of the essence in this Agreement.</span></div>
      <div class="clause"><b>25.</b><span>This Agreement may be executed in counterpart.</span></div>
      <div class="clause"><b>26.</b><span>Headings are inserted for the convenience of the parties only and are not to be considered when interpreting this Agreement. Words in the singular mean and include the plural and vice versa. Words in the masculine mean and include the feminine and vice versa.</span></div>
      <div class="clause"><b>27.</b><span>The clauses, paragraphs, and subparagraphs contained in this Agreement are intended to be read and construed independently of each other. If any part of this Agreement is held to be invalid, this invalidity will not affect the operation of any other part of this Agreement.</span></div>
    </div>
    <footer class="page-foot"><span>©2024 Terravane Legal // 7</span></footer>
  </article>

  <!-- Page 8 -->
  <article class="page" style="left:801px;top:1839px">
    <header class="page-head"><div class="brand"><span class="brand-dot"></span><div class="brand-text"><div class="brand-name">Terravane</div><div class="brand-tag">Spatial Security Intelligence</div></div></div></header>
    <svg class="page-pin" width="26" height="32" viewBox="0 0 34 42" aria-hidden="true"><path d="M17 1C8 1 2 8 2 16c0 11 15 25 15 25s15-14 15-25C32 8 26 1 17 1z" fill="#cfcfcf"/><circle cx="17" cy="16" r="6" fill="#fff"/></svg>
    <div class="page-body" style="top:76px">
      <div class="clause"><b>28.</b><span>The Evaluator is liable for all costs, expenses and expenditures including, and without limitation, the complete legal costs incurred by the Company in enforcing this Agreement as a result of any default of this Agreement by the Evaluator.</span></div>
      <div class="clause"><b>29.</b><span>The Company and the Evaluator acknowledge that this Agreement is reasonable, valid and enforceable. However, if a court of competent jurisdiction finds any of the provisions of this Agreement to be too broad to be enforceable, it is the intention of the Company and the Evaluator that such provision be reduced in scope by the court only to the extent deemed necessary by that court to render the provision reasonable and enforceable, bearing in mind that it is the intention of the Evaluator to give the Company the broadest possible protection against disclosure of the Confidential Information.</span></div>
      <div class="clause"><b>30.</b><span>No failure or delay by the Company in exercising any power, right or privilege provided in this Agreement will operate as a waiver, nor will any single or partial exercise of such rights, powers or privileges preclude any further exercise of them or the exercise of any other right, power or privilege provided in this Agreement.</span></div>
      <div class="clause"><b>31.</b><span>This Agreement will inure to the benefit of and be binding upon the respective heirs, executors, administrators, successors and assigns, as the case may be, of the Company and the Evaluator.</span></div>
      <div class="clause"><b>32.</b><span>This Agreement constitutes the entire agreement between the parties and there are no further items or provisions, either oral or otherwise.</span></div>
      <p style="margin-top:10px"><b>IN WITNESS WHEREOF</b> Northline Labs and COMPANY NAME have duly affixed their signatures under hand and seal</p>
      <div class="dated" style="margin-top:6px">This <i></i> day of <i></i></div>
      <div class="sign" style="margin-top:16px">
        <div class="row"><span><b>Name:</b></span><i>Northline Labs</i></div>
        <div class="row"><span>Per:<br>(Seal)</span><i></i></div>
      </div>
      <div class="sign" style="margin-top:26px">
        <div class="row"><span><b>Name:</b></span><i></i></div>
        <div class="row"><span>Per:<br>(Seal)</span><i></i></div>
      </div>
    </div>
    <footer class="page-foot"><span>©2024 Terravane Legal // 8</span></footer>
  </article>

  <!-- Back cover -->
  <section class="back">
    <span class="disc"></span>
    <div class="name">Terravane</div>
    <div class="web">www.terravane-secure.com</div>
  </section>
</main>
</body>
</html>
```